Business Cards - Brightway Harbor

need to design unique business card for my mortgage business. I need to design credit card style business card for my business or any unique idea that you might have

Target Market(s)

Home Loan customers

Industry/Entity Type

Mortgage Brokerage

Contact Information for Business Card

please design credit card style or very unique style business card

Colors

Designer to choose colors to be used in the design.

Requirements
Must have
• Name
• position
• Phone number
• fax number
• email address
• website address
• social media address
• All above fields will be provided once design in finalised

```html
<!DOCTYPE html>
<html lang="en">
<head>
<meta charset="utf-8">
<title>Brightway Harbor – Card Style Business Card</title>
<link href="https://fonts.googleapis.com/css2?family=Questrial&family=Didact+Gothic&display=swap" rel="stylesheet">
<style>
  :root {
    --canvas-bg: #b4b4b4;
    --card-light: #eeeef0;
    --card-mid: #cfd0d3;
    --card-dark: #a9aaae;
    --ink: #1a1a1a;
    --ink-soft: #3a3a3a;
    --emboss-face: #dcdcde;
    --emboss-edge: #5e5e62;
    --stripe: #111111;
    --panel: #ffffff;
  }
  * { box-sizing: border-box; margin: 0; padding: 0; }
  html, body { width: 1200px; height: 900px; overflow: hidden; }
  body {
    background: var(--canvas-bg);
    font-family: "Questrial", "Didact Gothic", sans-serif;
    color: var(--ink);
    position: relative;
  }
  .card {
    position: absolute;
    top: 278px;
    width: 540px;
    height: 340px;
    border-radius: 22px;
    background: linear-gradient(125deg, var(--card-light) 0%, var(--card-mid) 55%, var(--card-dark) 100%);
    box-shadow: 0 6px 18px rgba(0,0,0,0.25);
    overflow: hidden;
  }
  .card--back { left: 40px; }
  .card--front { left: 620px; }

  /* Back */
  .back-address {
    position: absolute; top: 16px; left: 24px;
    font-size: 15px; letter-spacing: 0.5px; color: var(--ink-soft);
  }
  .mag-stripe {
    position: absolute; top: 44px; left: 0; right: 0; height: 58px;
    background: var(--stripe);
  }
  .signature-panel {
    position: absolute; top: 122px; left: 64px; width: 440px; height: 52px;
    background: var(--panel);
  }
  .signature-note {
    position: absolute; top: 184px; left: 64px;
    font-size: 10px; letter-spacing: 0.6px; color: var(--ink-soft);
  }
  .back-brand { position: absolute; left: 214px; top: 218px; }

  /* Brand lockup */
  .brand-name {
    display: flex; align-items: center; gap: 8px;
    font-size: 30px; letter-spacing: 1px; color: var(--ink); line-height: 1;
  }
  .brand-mark { width: 14px; height: 14px; background: var(--ink); }
  .brand-tagline { font-size: 12px; margin-top: 6px; color: var(--ink); }
  .brand-web { font-size: 15px; margin-top: 10px; letter-spacing: 0.5px; color: var(--ink-soft); }

  /* Front */
  .front-brand { position: absolute; top: 26px; right: 30px; text-align: right; }
  .front-brand .brand-name { justify-content: flex-end; }
  .chip { position: absolute; top: 124px; left: 40px; }
  .emboss {
    color: var(--emboss-face);
    text-shadow: -1px -1px 0 #ffffff, 1px 1px 0 var(--emboss-edge), 2px 2px 2px rgba(0,0,0,0.35);
  }
  .office-line {
    position: absolute; top: 126px; left: 250px;
    display: flex; align-items: center; gap: 8px; font-size: 24px; letter-spacing: 1.5px;
  }
  .office-line .divider { width: 2px; height: 22px; background: var(--emboss-edge); margin-right: 4px; }
  .valid {
    position: absolute; top: 182px; right: 40px; display: flex; align-items: flex-end; gap: 6px;
  }
  .valid-label { font-size: 9px; color: var(--ink-soft); line-height: 1.1; margin-bottom: 3px; }
  .valid-date { display: flex; flex-direction: column; align-items: flex-start; }
  .valid-date small { font-size: 6px; color: var(--ink-soft); letter-spacing: 0.3px; }
  .valid-date span { font-size: 17px; color: var(--ink-soft); letter-spacing: 1px; }
  .contact-list { position: absolute; top: 182px; left: 40px; list-style: none; }
  .contact-item { display: flex; align-items: center; gap: 8px; margin-bottom: 6px; }
  .contact-item--mobile { font-size: 24px; letter-spacing: 1.5px; }
  .contact-item--email, .contact-item--fax { font-size: 17px; font-weight: bold; color: var(--ink); }
  .contact-item svg { flex: none; }
  .holder { position: absolute; left: 40px; bottom: 18px; }
  .holder-name { font-size: 26px; letter-spacing: 1.5px; line-height: 1.1; }
  .holder-title { font-size: 18px; letter-spacing: 1px; line-height: 1.2; }
</style>
</head>
<body>

<section class="card card--back" aria-label="Card back">
  <p class="back-address">000. Any Street, Anywhere, ST 0000</p>
  <div class="mag-stripe"></div>
  <div class="signature-panel"></div>
  <p class="signature-note">AUTHORIZED SIGNATURE / NOT VALID UNLESS SIGNED</p>
  <div class="back-brand">
    <div class="brand-name"><span class="brand-mark"></span>Brightway Harbor</div>
    <p class="brand-tagline">Home loans made simple</p>
    <p class="brand-web">www.yourwebsite.com</p>
  </div>
</section>

<section class="card card--front" aria-label="Card front">
  <div class="front-brand">
    <div class="brand-name"><span class="brand-mark"></span>Brightway Harbor</div>
    <p class="brand-tagline">Home loans made simple</p>
    <p class="brand-web">www.yourwebsite.com</p>
  </div>

  <svg class="chip" width="54" height="42" viewBox="0 0 54 42" aria-hidden="true">
    <defs>
      <linearGradient id="chipGold" x1="0" y1="0" x2="1" y2="1">
        <stop offset="0" stop-color="#f3dc8f"/>
        <stop offset="1" stop-color="#c79a3c"/>
      </linearGradient>
    </defs>
    <rect x="0.5" y="0.5" width="53" height="41" rx="6" fill="url(#chipGold)" stroke="#9c7a2e"/>
    <path d="M0 14 H17 M0 28 H17 M37 14 H54 M37 28 H54 M17 6 V36 M37 6 V36 M17 6 H37 M17 36 H37" stroke="#8d6c25" stroke-width="1.3" fill="none"/>
  </svg>

  <div class="office-line emboss">
    <span class="divider"></span>
    <svg width="22" height="18" viewBox="0 0 22 18" aria-hidden="true">
      <path d="M2 6 Q11 -1 20 6 L17 8 L14 6 L8 6 L5 8 Z" fill="#5e5e62"/>
      <rect x="4" y="9" width="14" height="8" rx="1" fill="#5e5e62"/>
      <circle cx="11" cy="13" r="2" fill="#dcdcde"/>
    </svg>
    <span>000 000 0000</span>
  </div>

  <div class="valid">
    <span class="valid-label">VALID THRU</span>
    <span class="valid-date"><small>MONTH/YEAR</small><span>07/15</span></span>
  </div>

  <ul class="contact-list">
    <li class="contact-item contact-item--mobile emboss">
      <svg width="16" height="26" viewBox="0 0 16 26" aria-hidden="true">
        <rect x="1" y="1" width="14" height="24" rx="3" fill="none" stroke="#5e5e62" stroke-width="2"/>
        <line x1="5" y1="21" x2="11" y2="21" stroke="#5e5e62" stroke-width="1.5"/>
      </svg>
      <span>000 000 0000</span>
    </li>
    <li class="contact-item contact-item--email">
      <svg width="22" height="15" viewBox="0 0 22 15" aria-hidden="true">
        <rect x="0" y="0" width="22" height="15" fill="#1a1a1a"/>
        <path d="M1 1 L11 9 L21 1" stroke="#dcdcde" stroke-width="1.5" fill="none"/>
      </svg>
      <span>youremail@sample.com</span>
    </li>
    <li class="contact-item contact-item--fax">
      <svg width="22" height="18" viewBox="0 0 22 18" aria-hidden="true">
        <rect x="6" y="0" width="10" height="6" fill="#1a1a1a"/>
        <rect x="0" y="6" width="22" height="12" rx="2" fill="#1a1a1a"/>
        <rect x="4" y="10" width="10" height="2" fill="#dcdcde"/>
      </svg>
      <span>000 000 0000</span>
    </li>
  </ul>

  <div class="holder emboss">
    <p class="holder-name">YOUR NAME</p>
    <p class="holder-title">JOB TITLE</p>
  </div>
</section>

</body>
</html>
```